Design Briefpapier
Zielgruppe
Veranstaltungstechnik
Aufgabenstellung
Wir möchten unser Layout (Briefkopf, Header, Footer) neu gestalten lassen. Es existiert bereits ein Logo, das leicht verändert im Header erscheinen soll! WICHTIG: Das Logo soll schwarz hinterlegt werden auf dem Briefpapier, damit das eigentliche Design (orange auf schwarz) auch zur Geltung kommt.
Wir benötigen Briefpapier: Anschreiben, Rechnngsformular in Farbe und in schwarz weiß. Dazu Visitenkarten und ein gleicherscheinenden E-Mail Absender. Das Design sollte so klar wir möglich sein. Der Druck erfolgt auf recyceltem Papier.
Wir benötigen ein Briefpapierbogen sowie ein Visitenkarten Design! Folgende Angaben müssen auf dem Briefpapier sein: - Logo (siehe Anhang) - Anschrift (KT Werkhaus UG (haftungsbeschränkt), Tanne 7, 75318 Wolfach - Wasserzeichen - GF (Jörg Pellinger) - Bankverbindung ( IBAN DE48 2917 5530..
Wir bitten um ein Design für unser Briefpapier. Wir suchen ein hochwertiges Design, das die Werte Vertrauen, Exklusivität und Innovation ausstrahlt. Es soll edel aussehen. Bitte für Telefon, Mail etc. Icons benutzen, damit es für jedermann verständlich ist, unabhängig von der Sprach..
Es sollte clean sein, Farben wie , Weiß, blau, grün, wären von Vorteil. Habe keine besondere Vorstellungen lasse mich gerne überraschen. Siehe .. www.vorkast.de
Bitte inklusive Logo (sollte Recht, Digital/Apps, Medizin illustrieren) - habe das Preisgeld vor diesem Hintergrund erhöht. ------------------------- Die Kanzlei arbeitet an der Schnittstelle von (Medizin-)Recht und Digital. Von daher wären wären Symbole/Gestaltung aus Bereich Medizin, Recht..

```html
<!DOCTYPE html>
<html lang="de">
<head>
<meta charset="utf-8">
<title>hallerwenke – Briefpapier und Visitenkarten</title>
<link href="https://fonts.googleapis.com/css2?family=Jost:wght@400;500;600&display=swap" rel="stylesheet">
<style>
  :root {
    --stage: #4a4a4a;
    --ink: #2a2627;
    --ink-light: #383435;
    --orange: #f58220;
    --paper: #ffffff;
    --mark-faint: #f4f4f4;
    --white: #ffffff;
  }
  * { margin: 0; padding: 0; box-sizing: border-box; }
  html, body { width: 1200px; height: 873px; overflow: hidden; }
  body { background: var(--stage); font-family: "Jost", sans-serif; position: relative; }

  .letterhead { position: absolute; left: 159px; top: 74px; width: 541px; height: 711px; background: var(--paper); }
  .letterhead__header, .letterhead__footer { position: absolute; left: 0; width: 100%; height: 54px; background: var(--ink); }
  .letterhead__header { top: 0; }
  .letterhead__footer { bottom: 0; }
  .accent-bar { position: absolute; left: 251px; top: 0; width: 40px; height: 100%; background: var(--orange); }

  .brand { position: absolute; display: flex; align-items: center; color: var(--white); font-weight: 500; letter-spacing: 0.2px; }
  .brand__dot { border-radius: 50%; background: var(--orange); flex: none; }
  .letterhead .brand { left: 32px; top: 14px; font-size: 23px; gap: 9px; }
  .letterhead .brand__dot { width: 19px; height: 19px; }

  .small-print { position: absolute; color: var(--orange); font-size: 6.4px; line-height: 7.6px; }
  .header-address { left: 312px; top: 12px; }
  .header-contact { left: 429px; top: 12px; }
  .sender-line { left: 52px; top: 156px; font-size: 6.2px; }
  .date-line { left: 423px; top: 156px; font-size: 6.2px; }

  .watermark { position: absolute; left: 86px; top: 171px; width: 370px; height: 370px; border-radius: 50%; background: var(--mark-faint); }

  .footer-bank { left: 52px; top: 13px; }
  .footer-tax { left: 397px; top: 13px; }
  .kv { display: grid; grid-template-columns: 50px auto; }
  .footer-tax .kv { grid-template-columns: 48px auto; }

  .card { position: absolute; left: 766px; width: 333px; height: 229px; background: linear-gradient(to top right, var(--ink) 50%, var(--ink-light) 50%); overflow: hidden; }
  .card--front { top: 125px; }
  .card--back { top: 444px; }
  .card__tab { position: absolute; left: 131px; width: 71px; height: 11px; background: var(--orange); }
  .card__tab--top { top: 0; }
  .card__tab--bottom { top: 216px; }
  .card-emblem { position: absolute; left: 97px; top: 45px; width: 140px; height: 140px; border-radius: 50%; background: var(--orange); }

  .card--back .brand { left: 38px; top: 62px; font-size: 30px; gap: 12px; }
  .card--back .brand__dot { width: 26px; height: 26px; }
  .card-person { position: absolute; left: 0; width: 100%; top: 121px; text-align: center; color: var(--white); }
  .card-person__name { font-size: 13px; font-weight: 500; line-height: 15px; }
  .card-person__role { font-size: 8.5px; font-weight: 500; }
  .card-band { position: absolute; left: 0; bottom: 0; width: 100%; height: 56px; background: var(--orange); border-top: 3px solid var(--white); }
  .card-band p { position: absolute; top: 9px; color: var(--ink); font-size: 9.6px; line-height: 10.6px; font-weight: 500; }
  .card-band__address { left: 25px; }
  .card-band__contact { left: 197px; }
</style>
</head>
<body>
  <article class="letterhead">
    <header class="letterhead__header">
      <div class="brand"><span class="brand__dot"></span>hallerwenke</div>
      <div class="accent-bar"></div>
      <p class="small-print header-address">hallerwenke GmbH &amp; Co. KG<br>Lindenweg 14<br>04109 Leipzig</p>
      <p class="small-print header-contact">Tel. 0341 218 770 12<br>Fax 0341 218 770 13<br>info@hallerwenke-audio.de</p>
    </header>

    <p class="small-print sender-line">hallerwenke GmbH &amp; Co. KG, Lindenweg 14, 04109 Leipzig</p>
    <p class="small-print date-line">Leipzig, den</p>
    <div class="watermark" role="img" aria-label="Dezentes Wasserzeichen"></div>

    <footer class="letterhead__footer">
      <div class="accent-bar"></div>
      <div class="small-print footer-bank">
        <div class="kv"><span>Bankverbindung:</span><span>Nordtal Bank</span></div>
        <div class="kv"><span>Kontonummer:</span><span>041827730</span></div>
        <div class="kv"><span>Bankleitzahl:</span><span>86051920</span></div>
        <div class="kv"><span>IBAN:</span><span>DE31860519200041827730</span></div>
      </div>
      <div class="small-print footer-tax">
        <div class="kv"><span>Steuernummer:</span><span>23/517/08361</span></div>
        <div class="kv"><span>USt-ID Nr:</span><span>DE318462097</span></div>
        <div class="kv" style="margin-top:7.6px"><span>BIC(SWIFT):</span><span>NRDT DE LX860</span></div>
      </div>
    </footer>
  </article>

  <section class="card card--front">
    <div class="card__tab card__tab--top"></div>
    <div class="card-emblem"></div>
    <div class="card__tab card__tab--bottom"></div>
  </section>

  <section class="card card--back">
    <div class="card__tab card__tab--top"></div>
    <div class="brand"><span class="brand__dot"></span>hallerwenke</div>
    <div class="card-person">
      <p class="card-person__name">Name Surname</p>
      <p class="card-person__role">President</p>
    </div>
    <div class="card-band">
      <p class="card-band__address">hallerwenke GmbH &amp; Co. KG<br>Lindenweg 14<br>04109 Leipzig</p>
      <p class="card-band__contact">Tel. 0341 218 770 12<br>Fax 0341 218 770 13<br>info@hallerwenke-audio.de</p>
    </div>
  </section>
</body>
</html>
```